2021 Beatwalker's Statute Compendium

Each year I public a law book for Massachusetts Police Officers, along with an accompanying motor vehicle cruiser guide. They have the same/similar design but the motor vehicle guide has a motor vehicle twist to it. The main book with be full-size with a front, back and spine. The accompanying cruiser guide will be smaller 5X7 with a spiral binding.
The year should be somewhat prominent so people know it is a new year edition. I attached some previous versions and commonly used logos.

Target Market(s)

Police Departments, Police Officers

Requirements
Must have
• Accompanying motor vehicle cruiser guide design, can be the same with a slight modification to gear it toward motor vehicle laws/rules.

The year of publishing - 2021
Nice to have
• Real images
Should not have
• Foreign (non-US) images of police.

```html
<!DOCTYPE html>
<html lang="en">
<head>
<meta charset="utf-8">
<title>2021 Beatwalker's Statute Compendium</title>
<link href="https://fonts.googleapis.com/css2?family=Oswald:wght@600&family=Prata&display=swap" rel="stylesheet">
<style>
  :root {
    --stage: #9a9a9a;
    --cover-blue: #0b56b3;
    --cover-blue-deep: #0847a0;
    --navy: #0a0f3c;
    --navy-mid: #16267a;
    --band-navy: #1f2159;
    --gold-light: #f7d774;
    --gold: #e0a92a;
    --gold-dark: #b07a12;
    --bar-yellow: #f4c13a;
    --bullet-red: #f0542a;
    --bar-text: #1d4fa8;
    --white: #ffffff;
  }
  * { margin: 0; padding: 0; box-sizing: border-box; }
  html, body {
    width: 1200px; height: 1200px; overflow: hidden;
    background: var(--stage);
  }
  .cover {
    position: absolute; left: 192px; top: 30px;
    width: 815px; height: 1140px; overflow: hidden;
    background:
      repeating-linear-gradient(0deg, rgba(255,255,255,0.04) 0 2px, transparent 2px 4px),
      linear-gradient(180deg, var(--cover-blue) 0%, var(--cover-blue-deep) 100%);
  }
  .cover-photo {
    position: absolute; left: 0; top: 44px;
    width: 660px; height: 1096px;
    border-radius: 0 240px 0 0;
    background: linear-gradient(180deg, var(--navy) 0%, var(--navy-mid) 45%, #1c3a8f 70%, #6f86b8 88%, #2a3560 100%);
  }
  .brand {
    position: absolute; left: 0; width: 590px; top: 236px;
    display: flex; align-items: center; justify-content: center; gap: 10px;
    font-family: "Oswald", sans-serif; font-weight: 600;
    font-size: 24px; letter-spacing: 2px; color: var(--gold);
    text-transform: uppercase;
  }
  .brand-dot {
    width: 14px; height: 14px; border-radius: 50%; background: var(--gold);
  }
  .title {
    position: absolute; left: 145px; top: 350px; width: 302px; height: 280px;
    overflow: visible;
  }
  .title text { font-family: "Oswald", sans-serif; font-weight: 600; }
  .guide-heading {
    position: absolute; left: 547px; top: 730px;
    font-family: "Prata", serif; font-weight: 400; font-size: 24px; line-height: 40px;
    color: var(--white); text-transform: uppercase;
  }
  .topic-list { list-style: none; }
  .topic {
    position: absolute; right: 0; height: 29px;
    background: var(--bar-yellow);
    font-family: "Prata", serif; font-size: 22px; line-height: 29px;
    color: var(--bar-text);
  }
  .topic::before {
    content: ""; position: absolute; top: 10px;
    width: 11px; height: 11px; border-radius: 50%; background: var(--bullet-red);
  }
  .topic span { position: absolute; white-space: nowrap; }
  .topic-1 { top: 852px; left: 497px; }
  .topic-2 { top: 889px; left: 543px; }
  .topic-3 { top: 926px; left: 500px; }
  .topic-4 { top: 962px; left: 476px; }
  .topic-1 span { left: 77px; } .topic-1::before { left: 55px; }
  .topic-2 span { left: 31px; } .topic-2::before { left: 9px; }
  .topic-3 span { left: 74px; } .topic-3::before { left: 52px; }
  .topic-4 span { left: 98px; } .topic-4::before { left: 76px; }
  .author-band {
    position: absolute; left: 0; top: 1062px; width: 815px; height: 43px;
    background: var(--band-navy);
    font-family: "Prata", serif; font-size: 32px; line-height: 43px;
    color: var(--white); text-align: center;
  }
</style>
</head>
<body>
  <main class="cover">
    <div class="cover-photo" role="img" aria-label="Silhouette of a police officer in a peaked cap, filled with a night city skyline and a patrol cruiser with blue lights"></div>

    <div class="brand"><span class="brand-dot"></span>Kestrel Ridge Consulting</div>

    <svg class="title" viewBox="0 0 302 280" aria-label="Beatwalker's Statute Compendium 2021">
      <defs>
        <linearGradient id="goldFill" x1="0" y1="0" x2="0" y2="1">
          <stop offset="0" stop-color="#f7d774"/>
          <stop offset="0.45" stop-color="#e0a92a"/>
          <stop offset="0.55" stop-color="#b07a12"/>
          <stop offset="1" stop-color="#f7d774"/>
        </linearGradient>
      </defs>
      <text x="0" y="42" font-size="51" textLength="302" lengthAdjust="spacingAndGlyphs" fill="url(#goldFill)">BEATWALKER'S STATUTE</text>
      <text x="0" y="105" font-size="68" textLength="302" lengthAdjust="spacingAndGlyphs" fill="url(#goldFill)">COMPENDIUM</text>
      <text x="0" y="273" font-size="198" textLength="302" lengthAdjust="spacingAndGlyphs" fill="url(#goldFill)">2021</text>
    </svg>

    <h2 class="guide-heading">Massachuetts<br>Police Officers<br>Guide To:</h2>

    <ul class="topic-list">
      <li class="topic topic-1"><span>Criminal Procedure,</span></li>
      <li class="topic topic-2"><span>Statutory Law,</span></li>
      <li class="topic topic-3"><span>Motor Vehicle Law</span></li>
      <li class="topic topic-4"><span>Juvenile Law</span></li>
    </ul>

    <p class="author-band">Dorian P. Whitcombe, ESQ.</p>
  </main>
</body>
</html>
```